Waste management company seeks a new website design

We need a website design for an environmental services company called 'Rannamõisa Jäätmehooldus.' We manage waste collection and recycling for 100K+ households and businesses across Estonia. Please use logos and colors from attached CVI file. The design should be extensively usable for our self-service portal and have a mobile-first approach as it will be turned into an app in the future. The new website should highlight our commitment to sustainability and provide easy access to our services with a clean, modern design. UX inspiration from https://vorrix.eu/et-ee/

```html
<!DOCTYPE html>
<html lang="et">
<head>
<meta charset="utf-8">
<title>Rannamõisa Jäätmehooldus</title>
<link href="https://fonts.googleapis.com/css2?family=Lexend:wght@300;400&family=Poppins:wght@400;500;600;700&display=swap" rel="stylesheet">
<style>
:root{
  --lime:#d5de3a;
  --lime-soft:#f1f5c6;
  --lime-band:#eaed98;
  --mauve:#7d636a;
  --mauve-text:#7a5c64;
  --grey-bg:#f0ecec;
  --ink:#3d3335;
  --footer:#353435;
  --footer-deep:#242324;
  --white:#ffffff;
}
*{box-sizing:border-box;margin:0;padding:0}
html,body{width:1200px;height:4439px;overflow:hidden}
body{position:relative;background:var(--white);font-family:"Poppins",sans-serif;color:var(--ink)}
.abs{position:absolute}
.heading{font-family:"Lexend",sans-serif;font-weight:300;color:var(--mauve-text);line-height:1.05}
.copy{font-size:11px;line-height:25px;color:var(--ink)}
.btn{position:absolute;display:flex;align-items:center;justify-content:center;height:31px;border-radius:9px;font-size:10px;font-weight:700;text-transform:uppercase;letter-spacing:.2px}
.btn-lime{background:var(--lime);color:var(--mauve-text)}
.btn-mauve{background:var(--mauve);color:var(--white)}
.photo{position:absolute;border-radius:26px}

.topbar{left:0;top:0;width:1200px;height:50px;background:var(--lime)}
.topbar span{position:absolute;top:17px;font-size:11.5px;color:var(--mauve-text)}
.topbar .active{font-weight:600;color:#2c2a1a}
.header{left:0;top:50px;width:1200px;height:81px;background:var(--white)}
.brand{position:absolute;display:flex;align-items:center;gap:12px}
.brand i{display:block;border-radius:50%}
.brand b{font-weight:500;line-height:1.1}

.hero{left:0;top:131px;width:1200px;height:581px;background:var(--grey-bg)}

.card{position:absolute;left:95px;width:1010px;height:403px;border-radius:30px}

.stat{position:absolute;top:2296px;width:193px;height:131px;background:var(--white);border-radius:18px;box-shadow:0 8px 26px rgba(0,0,0,.06);text-align:center}
.stat b{display:block;margin-top:30px;font-size:35px;font-weight:600;color:var(--mauve-text);line-height:1}
.stat span{display:block;margin-top:12px;font-size:11px;color:var(--ink)}

.contact-item{position:absolute;left:188px;display:flex;gap:20px}
.contact-item .ic{width:43px;height:43px;border-radius:9px;background:var(--lime);display:flex;align-items:center;justify-content:center}
.contact-item h4{font-size:11px;font-weight:600;margin-top:2px}
.contact-item p{font-size:8.5px;line-height:13px;color:#555}

.footer-nav span{position:absolute;top:4307px;font-size:11.5px;color:var(--white)}
</style>
</head>
<body>

<!-- top navigation -->
<div class="abs topbar">
  <span class="active" style="left:188px">Kodu</span>
  <span style="left:290px">Umbes</span>
  <span style="left:400px">Kodukliendid</span>
  <span style="left:547px">Äriklient</span>
  <span style="left:678px">Klienditugi</span>
  <span style="left:810px">Meie Ettevõte</span>
  <span style="left:959px">Meie Töö</span>
</div>

<div class="abs header">
  <div class="brand" style="left:188px;top:19px">
    <i style="width:44px;height:44px;background:var(--mauve)"></i>
    <b style="font-size:17px;color:var(--mauve-text)">Rannamõisa<br>Jäätmehooldus</b>
  </div>
  <div class="abs" style="left:804px;top:32px;display:flex;align-items:center;gap:6px;font-size:9px;color:var(--ink)">
    <i style="display:block;width:17px;height:17px;border-radius:50%;background:linear-gradient(#1d6fc4 0 33%,#111 33% 66%,#eee 66%)"></i>EN ▾
  </div>
  <div class="btn btn-mauve" style="left:872px;top:24px;width:140px;height:33px;border-radius:10px">Võtke Ühendust</div>
</div>

<!-- hero -->
<section class="abs hero"></section>
<h1 class="abs heading" style="left:188px;top:270px;font-size:38px">Uuenduslik<br>Keskkonnahooldus.</h1>
<p class="abs copy" style="left:188px;top:358px;width:390px">Lorem Ipsum On Lihtsalt Trüki- Ja Trükitööstuse Näiv Tekst. Lorem Ipsum On Olnud Tööstusharu Standardne Näidistekst Alates 1500. Aastatest, Kui Tundmatu Printer Võttis Tüübi Kambüüsi Ja Segas Selle, Et Koostada Tüübinäidise Raamat. See On Üle Elanud Mitte Ainult Viis Sajandit, Vaid Ka Hüppe Elektroonilisse Ladumisse, Jäädes Sisuliselt Muutumatuks.</p>
<div class="btn btn-lime" style="left:188px;top:536px;width:129px">Loe Rohkem</div>
<div class="photo" role="img" aria-label="Pine forest with a wooden boardwalk" style="left:659px;top:193px;width:386px;height:488px;background:linear-gradient(160deg,#9fc2d8,#4d6b3c 45%,#2f4426)"></div>
<div class="photo" role="img" aria-label="Rocky lake shore under a blue sky" style="left:895px;top:340px;width:320px;height:400px;border-radius:26px 0 0 26px;background:linear-gradient(180deg,#8fb8da,#c9dbe8 35%,#7e8c92 55%,#4e5f6a)"></div>

<!-- about / history -->
<div class="photo" role="img" aria-label="Smiling older woman with a backpack in an autumn forest" style="left:188px;top:788px;width:405px;height:376px;background:linear-gradient(160deg,#c7a679,#8a6a48 50%,#4a3a2c)"></div>
<i class="abs" style="left:120px;top:1104px;width:135px;height:118px;border-radius:50%;background:var(--mauve);opacity:.55"></i>
<h2 class="abs heading" style="left:665px;top:810px;font-size:35px">Keskkonnateenuste<br>Ettevõtte Ajalugu.</h2>
<p class="abs copy" style="left:665px;top:900px;width:345px">Rannamõisa Jäätmehooldus On Eesti Juhtiv Jäätmekäitlus- Ja Kommunaalteenuseid Pakkuv Kontsern, Mille Põhitegevuseks On Olmejäätmete Kogumine. Lisaks Sellele Tegeleb Ettevõte Teisese Toorme, Ehitusjäätmete Ning Muude Jäätmete Kogumisega. Mõningates Piirkondades Pakub Ettevõte Talvisel Ajal Ka Teede Ja Tänavate Hooldusteenust.</p>
<div class="btn btn-mauve" style="left:665px;top:1102px;width:130px">Meie Lugu</div>

<!-- household services -->
<section class="card" style="top:1240px;background:var(--lime-soft)"></section>
<h2 class="abs heading" style="left:188px;top:1322px;font-size:31px">Majapidamised Teenus</h2>
<p class="abs copy" style="left:188px;top:1370px;width:350px">Rannamõisa Jäätmehooldus On Eesti Juhtiv Jäätmekäitlus- Ja Kommunaalteenuseid Pakkuv Kontsern, Mille Põhitegevuseks On Olmejäätmete Kogumine. Lisaks Sellele Tegeleb Ettevõte Teisese Toorme, Ehitusjäätmete Ning Muude Jäätmete Kogumisega.</p>
<div class="btn btn-lime" style="left:188px;top:1522px;width:129px">Loe Rohkem</div>
<div class="photo" role="img" aria-label="People walking in a sunlit park path" style="left:590px;top:1314px;width:405px;height:255px;background:linear-gradient(160deg,#f2d28a,#9a7a3e 45%,#4b4221)"></div>

<!-- business services -->
<section class="card" style="top:1719px;background:var(--grey-bg)"></section>
<div class="photo" role="img" aria-label="Woman sitting on green grass in sunlight" style="left:188px;top:1793px;width:405px;height:255px;background:linear-gradient(160deg,#b7c35a,#5f8a2c 50%,#355a1e)"></div>
<h2 class="abs heading" style="left:662px;top:1800px;font-size:31px">Ettevõtted Üle Teenus</h2>
<p class="abs copy" style="left:662px;top:1848px;width:350px">Rannamõisa Jäätmehooldus On Eesti Juhtiv Jäätmekäitlus- Ja Kommunaalteenuseid Pakkuv Kontsern, Mille Põhitegevuseks On Olmejäätmete Kogumine. Lisaks Sellele Tegeleb Ettevõte Teisese Toorme, Ehitusjäätmete Ning Muude Jäätmete Kogumisega.</p>
<div class="btn btn-mauve" style="left:662px;top:2000px;width:129px">Loe Rohkem</div>

<!-- stats -->
<h2 class="abs heading" style="left:0;width:1200px;text-align:center;top:2190px;font-size:35px">Aitame Teil Oma Äri Kasvatada</h2>
<p class="abs" style="left:0;width:1200px;text-align:center;top:2248px;font-size:11px">Lorem Ipsum On Lihtsalt Trüki- Ja Trükitööstuse Näiv Tekst. Lorem Ipsum On.</p>
<div class="stat" style="left:188px"><b>100k+</b><span>Finished Products</span></div>
<div class="stat" style="left:398px"><b>50k+</b><span>Issues Solved</span></div>
<div class="stat" style="left:608px"><b>70k+</b><span>Happy Customers</span></div>
<div class="stat" style="left:817px"><b>25k+</b><span>Awwards Winning</span></div>

<!-- testimonials -->
<section class="abs" style="left:0;top:2503px;width:1200px;height:600px;background:var(--lime-band)"></section>
<i class="abs" style="left:958px;top:2535px;width:240px;height:220px;border-radius:50%;background:var(--white);opacity:.45"></i>
<h2 class="abs heading" style="left:0;width:1200px;text-align:center;top:2572px;font-size:35px">Mida Meie Klient Ütleb</h2>
<div class="abs" style="left:257px;top:2689px;width:686px;height:187px;background:var(--white);border-radius:14px"></div>
<p class="abs copy" style="left:463px;top:2730px;width:390px">Lorem Ipsum On Lihtsalt Trüki- Ja Trükitööstuse Näiv Tekst. Lorem Ipsum On Olnud Tööstusharu Standardne Näidistekst Alates 1500. Aastatest, Kui Tundmatu Printer Võttis Tüübi Kambüüsi Ja Segas Selle, Et Koostada Tüübinäidise Raamat.</p>
<div class="abs" style="left:241px;top:2641px;width:173px;height:198px;background:var(--mauve);border-radius:8px;text-align:center;color:var(--white)">
  <div role="img" aria-label="Portrait of the client" style="width:94px;height:94px;margin:33px auto 0;border-radius:50%;background:linear-gradient(#e8e4e4,#b9a9a8);border:3px solid var(--white)"></div>
  <div style="margin-top:12px;font-size:10px;font-weight:600">Mart Kask</div>
  <div style="font-size:10px">Creative Director</div>
</div>
<svg class="abs" style="left:826px;top:2641px" width="88" height="66" viewBox="0 0 88 66"><g fill="var(--lime)"><path d="M4 34c0-18 10-30 28-34l3 7c-9 4-13 10-13 17a18 18 0 1 1-18 10z"/><path d="M48 34c0-18 10-30 28-34l3 7c-9 4-13 10-13 17a18 18 0 1 1-18 10z"/></g></svg>
<svg class="abs" style="left:543px;top:2911px" width="120" height="42" viewBox="0 0 120 42"><g><circle cx="21" cy="21" r="20" fill="var(--lime)"/><circle cx="93" cy="21" r="20" fill="var(--lime)"/><path d="M29 21H13m6-6-6 6 6 6M85 21h16m-6-6 6 6-6 6" fill="none" stroke="var(--mauve)" stroke-width="2" stroke-linecap="round" stroke-linejoin="round"/></g></svg>

<!-- mission banner -->
<div class="abs" style="left:188px;top:3027px;width:824px;height:156px;background:var(--mauve);border-radius:18px"></div>
<i class="abs" style="left:212px;top:3052px;width:106px;height:106px;border-radius:50%;background:var(--lime)"></i>
<p class="abs" style="left:400px;top:3066px;width:520px;text-align:center;font-family:'Lexend',sans-serif;font-weight:300;font-size:35px;line-height:38px;color:var(--white)">“ We Care About Nature We Care About The Future “</p>

<!-- contact -->
<h2 class="abs heading" style="left:188px;top:3268px;font-size:37px">Ühendust Võtma</h2>
<p class="abs" style="left:188px;top:3326px;width:330px;font-size:11px;line-height:25px">Üle-Eestiline Infotelefoni Lühinumber - 1414 Lühinumbrile Helistades Kehtib Tavahind, Millele Lisandub.</p>
<div class="contact-item" style="top:3400px">
  <div class="ic"><svg width="20" height="24" viewBox="0 0 20 24"><path d="M10 1a8 8 0 0 0-8 8c0 6 8 14 8 14s8-8 8-14a8 8 0 0 0-8-8zm0 11a3 3 0 1 1 0-6 3 3 0 0 1 0 6z" fill="var(--mauve)"/></svg></div>
  <div><h4>Aadress</h4><p>Veerenni 42, Tallinn 10138,<br>Registrikood: 1048315</p></div>
</div>
<div class="contact-item" style="top:3482px">
  <div class="ic"><svg width="24" height="18" viewBox="0 0 24 18"><rect x="1" y="1" width="22" height="16" rx="2" fill="none" stroke="var(--mauve)" stroke-width="2"/><path d="M1 2l11 8 11-8" fill="none" stroke="var(--mauve)" stroke-width="2"/></svg></div>
  <div><h4>Email</h4><p>info@rannamoisa.ee</p></div>
</div>
<div class="contact-item" style="top:3565px">
  <div class="ic"><svg width="22" height="22" viewBox="0 0 24 24"><path d="M6.6 10.8a15 15 0 0 0 6.6 6.6l2.2-2.2a1 1 0 0 1 1-.25 11.4 11.4 0 0 0 3.6.57 1 1 0 0 1 1 1V20a1 1 0 0 1-1 1A17 17 0 0 1 3 4a1 1 0 0 1 1-1h3.5a1 1 0 0 1 1 1c0 1.25.2 2.45.57 3.57a1 1 0 0 1-.25 1z" fill="var(--mauve)"/></svg></div>
  <div><h4>Helistama</h4><p>(+372) 655 41 20</p></div>
</div>
<i class="abs" style="left:556px;top:3195px;width:90px;height:130px;border-radius:50%;background:var(--mauve);opacity:.7"></i>
<div class="photo" role="img" aria-label="Aerial view of a forested coastline and turquoise sea" style="left:607px;top:3258px;width:405px;height:368px;background:linear-gradient(175deg,#7e93a3,#b9c6cc 30%,#3f8f99 55%,#2f4a2c 80%)"></div>
<i class="abs" style="left:930px;top:3600px;width:130px;height:58px;border-radius:50%;background:var(--lime)"></i>

<!-- careers -->
<div class="abs" role="img" aria-label="Wind turbines on a misty hillside" style="left:95px;top:3700px;width:1010px;height:343px;border-radius:30px;background:linear-gradient(100deg,#8e8190,#9c909a 50%,#6d6a5e)"></div>
<i class="abs" style="left:730px;top:3770px;width:280px;height:250px;border-radius:50%;background:var(--lime)"></i>
<h2 class="abs heading" style="left:188px;top:3775px;font-size:37px;color:var(--white)">Tule Tööle!</h2>
<p class="abs" style="left:188px;top:3828px;width:345px;font-size:11px;line-height:25px;color:var(--white)">Ootame Oma Meeskonda Tublisid Ja Töökaid Inimesi. Meie Ettevõttesse Saab Kandideerida Läbi Tööotsija Portaali - Vaata Kõiki Aktiivseid Töökuulutusi.</p>
<div class="btn btn-lime" style="left:188px;top:3929px;width:150px">Kandideeri Kohe</div>

<!-- footer -->
<footer class="abs" style="left:0;top:4117px;width:1200px;height:279px;background:var(--footer)"></footer>
<div class="brand" style="left:188px;top:4198px">
  <i style="width:60px;height:60px;background:var(--white)"></i>
  <b style="font-size:25px;color:var(--white)">Rannamõisa<br>Jäätmehooldus</b>
</div>
<div class="abs" style="left:860px;top:4215px;display:flex;gap:10px">
  <i style="display:block;width:30px;height:30px;border-radius:50%;background:var(--lime)"></i>
  <i style="display:block;width:30px;height:30px;border-radius:50%;background:var(--lime)"></i>
  <i style="display:block;width:30px;height:30px;border-radius:50%;background:var(--lime)"></i>
  <i style="display:block;width:30px;height:30px;border-radius:50%;background:var(--lime)"></i>
</div>
<div class="footer-nav">
  <span style="left:188px;font-weight:600">Kodu</span><span style="left:251px">/</span>
  <span style="left:290px">Umbes</span><span style="left:363px">/</span>
  <span style="left:400px">Kodukliendid</span><span style="left:509px">/</span>
  <span style="left:547px">Äriklient</span><span style="left:640px">/</span>
  <span style="left:678px">Klienditugi</span><span style="left:772px">/</span>
  <span style="left:810px">Meie Ettevõte</span><span style="left:921px">/</span>
  <span style="left:959px">Meie Töö</span>
</div>
<div class="abs" style="left:0;top:4396px;width:1200px;height:43px;background:var(--footer-deep);color:var(--white);font-size:11px;text-align:center;line-height:43px">© Autoriõigus 2024. <b>Rannamõisa Jäätmehooldus</b> Kõik Õigused Kaitstud</div>

</body>
</html>
```